Talkbridge Allies co-marketing flier

We want a flier that our partners (IT consultants) can hand out to their clients and that we can send to local businesses on their behalf to demonstrate that they can help customers purchase a phone system that has professional features that they would expect in a phone solution that costs thousands of dollars.

We want the brochure to look very professional with excellent layout and use of space.

The Talkbridge Allies corporate colour is green and more details can be found at www.talkbridgeallies.com.au.

We have attached a draft Word document that contains most of the information we need but please present the information in the way YOU believe it should be laid out.

We are looking for a designer who understands the concept and uses their own skills to produce a work of art.

Target Market(s)

small businesses that want to save money but also want a modern phone with lots of features

Industry/Entity Type

Marketing

Requirements
Must have
• Must have an image of the main phone and a cordless handset to indicate that they don't need wires to set the system up.

Must have our logo and website address

Must have a box or some "placeholder" where our partners can stamp or insert their details.

Must have a "call to action" saying "Contact us for a quote"

```html
<!DOCTYPE html>
<html lang="en">
<head>
<meta charset="utf-8">
<title>Talkbridge Allies – New Phone System Flier</title>
<link rel="stylesheet" href="https://fonts.googleapis.com/css2?family=Russo+One&family=Oswald:wght@500;700&family=Arimo:wght@400;700&display=swap">
<style>
  :root {
    --green: #8cc63f;
    --green-light: #d4eab0;
    --green-deep: #2c8a3e;
    --green-soft: #9bcf86;
    --orange: #ee7a1c;
    --ink: #1d1d1d;
    --grey-text: #555;
    --grey-line: #d0d0d0;
    --grey-bracket: #c8c8c8;
    --tan: #b98a5d;
    --heading-dark: #444;
  }
  * { margin: 0; padding: 0; box-sizing: border-box; }
  html, body { width: 848px; height: 1200px; overflow: hidden; background: #fff; }
  .flier { position: relative; width: 848px; height: 1200px; font-family: "Arimo", Arial, sans-serif; overflow: hidden; }
  .bubbles { position: absolute; inset: 0; }
  .abs { position: absolute; }

  .header-photo {
    left: 0; top: 0; width: 215px; height: 210px;
    background: linear-gradient(135deg, #eaf5d8, #b5d98a);
  }
  .headline { left: 228px; top: 52px; font-family: "Russo One", sans-serif; line-height: 1; }
  .headline .lead {
    display: block; font-size: 47px; color: var(--ink);
    -webkit-text-stroke: 0; text-shadow: 0 0 3px #fff, 0 0 3px #fff, 0 0 3px #fff;
  }
  .headline .main {
    display: block; margin-top: 12px; font-size: 49px; color: var(--orange);
    text-shadow: 0 0 3px #fff, 0 0 3px #fff, 0 0 3px #fff;
  }
  .question { left: 724px; top: 82px; font-family: "Russo One", sans-serif; font-size: 96px; color: #e4e4e4; opacity: .85; line-height: 1; }

  .product-photo {
    left: 125px; top: 315px; width: 582px; height: 282px;
    background: radial-gradient(ellipse at center, #cfcfcf 0%, #eeeeee 60%, rgba(255,255,255,0) 100%);
  }

  .features-title { left: 150px; top: 618px; font-family: "Russo One", sans-serif; font-size: 29px; color: var(--green-deep); }
  .features-title small { font-family: "Arimo", sans-serif; font-size: 17px; color: var(--green-soft); margin-left: 10px; letter-spacing: .5px; }
  .bracket { top: 650px; font-family: "Arimo", sans-serif; font-size: 98px; color: var(--grey-bracket); line-height: 1; font-weight: 400; }
  .bracket.open { left: 113px; }
  .bracket.close { left: 705px; }
  .feature-list { list-style: none; font-size: 14.5px; color: #333; line-height: 20.5px; letter-spacing: .2px; }
  .feature-list li { position: relative; padding-left: 26px; white-space: nowrap; }
  .feature-list li::before {
    content: "\2713"; position: absolute; left: 2px; top: 0; color: var(--green-deep); font-size: 17px;
  }
  .list-left { left: 148px; top: 661px; }
  .list-right { left: 437px; top: 661px; }

  .pitch { left: 387px; top: 804px; width: 390px; font-size: 16px; line-height: 24px; color: var(--grey-text); letter-spacing: .3px; }
  .rule { left: 383px; top: 891px; width: 388px; height: 2px; background: var(--grey-line); }
  .cta-sub { left: 395px; top: 904px; font-family: "Oswald", sans-serif; font-weight: 700; font-size: 27px; color: var(--tan); }
  .cta-main { left: 394px; top: 940px; font-family: "Oswald", sans-serif; font-weight: 700; font-size: 38px; color: var(--heading-dark); }
  .stamp-box { left: 390px; top: 992px; }

  .brand { left: 110px; top: 1030px; display: flex; align-items: center; gap: 8px; font-family: "Arimo", sans-serif; font-weight: 700; font-size: 27px; color: var(--green-deep); }
  .brand .dot { width: 14px; height: 14px; border-radius: 50%; background: var(--green); }
  .company { right: 533px; top: 1085px; text-align: right; font-size: 14px; line-height: 22px; color: #333; letter-spacing: .4px; }
  .website { right: 533px; top: 1129px; font-size: 17px; color: var(--green-deep); letter-spacing: .8px; }
</style>
</head>
<body>
<main class="flier">
  <svg class="bubbles" width="848" height="1200" viewBox="0 0 848 1200" aria-hidden="true">
    <defs>
      <linearGradient id="headerGreen" x1="0" y1="0" x2="1" y2="0">
        <stop offset="0" stop-color="#e8f4d4"/>
        <stop offset=".45" stop-color="#b9de7a"/>
        <stop offset="1" stop-color="#84c22c"/>
      </linearGradient>
      <linearGradient id="bodyGrey" x1="0" y1="0" x2="0" y2="1">
        <stop offset="0" stop-color="#ffffff"/>
        <stop offset=".35" stop-color="#ffffff"/>
        <stop offset="1" stop-color="#d6d6d6"/>
      </linearGradient>
    </defs>
    <path class="body-bubble" d="M0 200 H848 V785 H372 L372 815 L320 785 H45 Q0 785 0 740 Z" fill="url(#bodyGrey)"/>
    <path class="header-bubble" d="M0 0 H848 V170 Q848 213 805 213 H598 L467 270 L492 213 H0 Z" fill="url(#headerGreen)"/>
    <path class="stamp-outline" d="M402 1007 H455 L470 995 L485 1007 H755 Q767 1007 767 1019 V1141 Q767 1153 755 1153 H403 Q391 1153 391 1141 V1019 Q391 1007 402 1007 Z" fill="#fff" stroke="#e3e3e3" stroke-width="2"/>
  </svg>

  <div class="abs header-photo" role="img" aria-label="Photo of business people reaching in with phone handsets around a smiling woman"></div>
  <h1 class="abs headline"><span class="lead">Looking for a</span><span class="main">NEW Phone System</span></h1>
  <div class="abs question" aria-hidden="true">?</div>

  <div class="abs product-photo" role="img" aria-label="Photo of a desk phone with colour screen beside a cordless handset in its charging cradle"></div>

  <h2 class="abs features-title">Features<small>include, but not limited to:</small></h2>
  <span class="abs bracket open" aria-hidden="true">[</span>
  <span class="abs bracket close" aria-hidden="true">]</span>
  <ul class="abs feature-list list-left">
    <li>Very low line rental rates</li>
    <li>10c local and national calls untimed</li>
    <li>Voicemail-to-email</li>
    <li>Bluetooth-to-mobile</li>
  </ul>
  <ul class="abs feature-list list-right">
    <li>Direct in-dial to every extension</li>
    <li>Keep your number when you move</li>
    <li>Call records via spreadsheet</li>
    <li>Flat rate local and national calls</li>
  </ul>

  <p class="abs pitch">Our proven VoIP solution comes with all the professional features to service an office of up to 6 people.</p>
  <div class="abs rule"></div>
  <p class="abs cta-sub">It’s Cheaper than you think.</p>
  <p class="abs cta-main">Contact us for a Quote</p>

  <div class="abs brand"><span class="dot"></span>Talkbridge Allies</div>
  <p class="abs company">kestrel (456 Holdings Pty Ltd)<br>ABN: 52 381 907 226</p>
  <p class="abs website">www.talkbridgeallies.com.au</p>
</main>
</body>
</html>
```